Service Plan Sales Flyer

The Watchpost Depot (www.kelvamart.com) is a commercial security integrator that installs security cameras, access control, intrusion, two-way radios and perimeter security. We require a one page flyer for our service plan for new and existing customers. The price of the service plan is $299/yr and includes the following;
1. Discounted service rate of $118/hr
2. Free remote support ($85/hr without a plan)
3. Free remote training
4. Priority support

Please review our brochure attached and create a one page sales flyer with the end goal of having the client sign up for our annual service plan . The plan will automatically renew every year. Email sales@kelvamart.com.

Target Market(s)

commercial industrial clients - no residential

Industry/Entity Type

review our website at www.kelvamart.com

Colors
0054AA
0677BA
7BADD7
CADEEF
E8F1F8
EE7325
F08F49
F5BC92
FAE3D3
FDF4ED

Requirements
Must have
• call to action
Should not have
• too many colors

```html
<!DOCTYPE html>
<html lang="en">
<head>
<meta charset="utf-8">
<title>The Watchpost Depot – Annual Service Plan</title>
<link href="https://fonts.googleapis.com/css2?family=Lato:wght@400;700;900&family=Oswald:wght@500;600&display=swap" rel="stylesheet">
<style>
  :root{
    --navy:#1d3560;
    --orange:#ee5b30;
    --white:#ffffff;
    --ink:#1d3560;
    --backdrop:#e9e9e9;
    --line:rgba(255,255,255,.45);
  }
  *{box-sizing:border-box;margin:0;padding:0}
  html,body{width:1200px;height:1200px;overflow:hidden;background:var(--backdrop)}
  body{font-family:"Lato",sans-serif;color:var(--ink)}
  .flyer{position:absolute;left:237px;top:87px;width:726px;height:1026px;background:var(--white);overflow:hidden;box-shadow:0 4px 18px rgba(0,0,0,.12)}
  .shapes{position:absolute;inset:0}
  .hero-photo{position:absolute;left:24px;top:14px;width:450px;height:300px;border-radius:4px;
    background:linear-gradient(135deg,rgba(255,255,255,.9),rgba(225,228,232,.85) 60%,rgba(190,196,204,.8))}
  .plan-title{position:absolute;left:540px;top:20px;width:180px;text-align:center;font-family:"Oswald",sans-serif;font-weight:600;font-size:41px;line-height:43px;color:var(--white);letter-spacing:.5px}
  .plan-price{position:absolute;left:520px;top:172px;width:206px;height:64px;text-align:center;font-family:"Oswald",sans-serif;font-weight:600;font-size:36px;line-height:64px;color:var(--white)}
  .plan-renew{position:absolute;left:520px;top:248px;width:206px;text-align:center;font-size:13px;line-height:16px;font-weight:700;color:var(--ink)}
  .includes-heading{position:absolute;left:480px;top:322px;width:246px;text-align:center;color:var(--orange);font-weight:900;font-size:19px;letter-spacing:5px}
  .includes-list{position:absolute;left:486px;top:362px;width:228px;list-style:none;color:var(--white);font-weight:700;font-size:17px;line-height:21px;text-transform:uppercase}
  .includes-list li{display:flex;gap:6px;padding:8px 0 10px 4px;border-bottom:1px solid var(--line)}
  .includes-list li:last-child{border-bottom:none}
  .cta{position:absolute;left:455px;top:698px;width:271px;text-align:center}
  .cta-title{font-family:"Oswald",sans-serif;font-weight:600;font-size:40px;line-height:44px;color:var(--orange)}
  .cta-text{font-weight:900;font-size:17px;line-height:21px;color:var(--ink);text-transform:uppercase}
  .cta-phone{position:absolute;left:440px;top:828px;width:286px;height:70px;display:flex;align-items:center;justify-content:center;gap:8px;font-family:"Oswald",sans-serif;font-weight:600;font-size:32px;color:var(--white)}
  .contact{position:absolute;left:458px;top:918px;font-weight:700;font-size:14px;line-height:17px;color:var(--ink)}
  .contact .web{display:block;margin-top:12px;font-weight:900;font-size:20px}
  .brand{position:absolute;left:30px;top:452px;width:380px;display:flex;align-items:center;gap:14px}
  .brand-mark{width:30px;height:30px;background:var(--navy);flex:none}
  .brand-name{font-weight:900;font-size:27px;line-height:30px;color:var(--navy);text-transform:uppercase;letter-spacing:.5px}
  .brand-tag{position:absolute;left:74px;top:492px;font-size:10px;font-weight:700;color:var(--navy)}
  .products-bar{position:absolute;left:30px;top:534px;width:262px;height:36px;color:var(--white);font-weight:900;font-size:22px;letter-spacing:5px;line-height:36px;padding-left:36px}
  .product{position:absolute;left:28px;display:flex;align-items:center;gap:18px;font-size:18px;line-height:21px;color:var(--ink);text-transform:uppercase}
  .product b{font-weight:900}
  .product svg{flex:none}
  .values{position:absolute;left:0;top:864px;width:414px;height:34px;text-align:center;color:var(--white);font-weight:900;font-size:18px;line-height:34px;letter-spacing:.5px}
  .service{position:absolute;display:flex;align-items:center;gap:14px;color:var(--white);font-weight:700;font-size:13px;text-transform:uppercase}
</style>
</head>
<body>
<main class="flyer">
  <svg class="shapes" width="726" height="1026" viewBox="0 0 726 1026" aria-hidden="true">
    <polygon points="0,0 440,0 476,160 230,372 0,278" fill="var(--orange)"/>
    <polyline points="0,300 236,398 500,162 474,94" fill="none" stroke="var(--navy)" stroke-width="3"/>
    <polygon points="530,0 726,0 726,170 520,170" fill="var(--navy)"/>
    <polygon points="506,170 726,170 726,238 506,238" fill="var(--orange)"/>
    <polygon points="470,300 726,300 726,690 442,690" fill="var(--navy)"/>
    <polygon points="442,690 456,690 440,1026 406,1026" fill="var(--navy)"/>
    <polygon points="440,828 726,828 726,898 438,898" fill="var(--orange)"/>
    <polygon points="30,534 292,534 292,570 30,570" fill="var(--navy)"/>
    <polygon points="300,534 308,534 300,570 292,570" fill="var(--orange)"/>
    <polygon points="0,864 414,864 412,898 0,898" fill="var(--orange)"/>
    <polygon points="0,898 412,898 406,1026 0,1026" fill="var(--navy)"/>
  </svg>

  <div class="hero-photo" role="img" aria-label="Security products: door, monitor showing camera software, dome camera and bullet camera"></div>

  <h1 class="plan-title">ANNUAL<br>SERVICE<br>PLAN</h1>
  <div class="plan-price">$299/yr</div>
  <p class="plan-renew">Automatically Renew<br>Every Year</p>

  <h2 class="includes-heading">INCLUDES</h2>
  <ol class="includes-list">
    <li><span>1.</span><span>Discounted service rate of $118/hr</span></li>
    <li><span>2.</span><span>Free remote support ($85/hr without a plan)</span></li>
    <li><span>3.</span><span>Free remote training</span></li>
    <li><span>4.</span><span>Priority support</span></li>
  </ol>

  <div class="cta">
    <h2 class="cta-title">CALL US</h2>
    <p class="cta-text">For your free quote<br>&amp; sign up for our<br>security plan.</p>
  </div>
  <div class="cta-phone">
    <svg width="30" height="30" viewBox="0 0 24 24" aria-hidden="true"><path d="M6.6 10.8a15.1 15.1 0 0 0 6.6 6.6l2.2-2.2a1 1 0 0 1 1-.25 11.4 11.4 0 0 0 3.6.57 1 1 0 0 1 1 1V20a1 1 0 0 1-1 1A17 17 0 0 1 3 4a1 1 0 0 1 1-1h3.5a1 1 0 0 1 1 1c0 1.25.2 2.45.57 3.57a1 1 0 0 1-.25 1z" fill="var(--white)"/></svg>
    <span>1-877-555-0142</span>
  </div>
  <address class="contact" style="font-style:normal">
    #12, 2870 Ridgeway Road SE<br>Fernvale, AB T0X 1A0<br>403-555-0187<br>403-555-0163
    <span class="web">www.kelvamart.com</span>
  </address>

  <div class="brand"><span class="brand-mark"></span><span class="brand-name">The Watchpost Depot</span></div>
  <p class="brand-tag" style="left:74px">Commercial &amp; Industrial Solutions</p>

  <h2 class="products-bar">PRODUCTS</h2>

  <div class="product" style="top:588px">
    <svg width="50" height="50" viewBox="0 0 50 50" aria-hidden="true"><circle cx="25" cy="25" r="25" fill="var(--orange)"/><circle cx="25" cy="25" r="20" fill="none" stroke="var(--white)" stroke-width="1.5"/><rect x="15" y="20" width="16" height="9" rx="2" fill="var(--white)"/><polygon points="31,22 36,19 36,30 31,27" fill="var(--white)"/></svg>
    <span>Security camera<br><b>System</b></span>
  </div>
  <div class="product" style="top:658px">
    <svg width="50" height="50" viewBox="0 0 50 50" aria-hidden="true"><circle cx="25" cy="25" r="25" fill="var(--orange)"/><circle cx="25" cy="25" r="20" fill="none" stroke="var(--white)" stroke-width="1.5"/><rect x="17" y="14" width="16" height="22" rx="2" fill="none" stroke="var(--white)" stroke-width="2"/><rect x="20" y="17" width="10" height="5" fill="var(--white)"/><circle cx="21" cy="27" r="1.3" fill="var(--white)"/><circle cx="25" cy="27" r="1.3" fill="var(--white)"/><circle cx="29" cy="27" r="1.3" fill="var(--white)"/><circle cx="21" cy="31" r="1.3" fill="var(--white)"/><circle cx="25" cy="31" r="1.3" fill="var(--white)"/><circle cx="29" cy="31" r="1.3" fill="var(--white)"/></svg>
    <span>Intrusion<br><b>Alarm</b></span>
  </div>
  <div class="product" style="top:728px">
    <svg width="50" height="50" viewBox="0 0 50 50" aria-hidden="true"><circle cx="25" cy="25" r="25" fill="var(--orange)"/><circle cx="25" cy="25" r="20" fill="none" stroke="var(--white)" stroke-width="1.5"/><circle cx="19" cy="20" r="5" fill="none" stroke="var(--white)" stroke-width="2.5"/><path d="M23 24l11 11M30 31l3-3M33 34l2-2" stroke="var(--white)" stroke-width="2.5"/></svg>
    <span>Access control<br><b>&amp; Intercom</b></span>
  </div>
  <div class="product" style="top:798px">
    <svg width="50" height="50" viewBox="0 0 50 50" aria-hidden="true"><circle cx="25" cy="25" r="25" fill="var(--orange)"/><circle cx="25" cy="25" r="20" fill="none" stroke="var(--white)" stroke-width="1.5"/><path d="M15 16v19M21 16v19M27 16v19M33 16v19M13 21h22M13 30h22" stroke="var(--white)" stroke-width="2"/></svg>
    <span>Perimeter<br><b>Security</b></span>
  </div>

  <p class="values">KNOWLEDGEABLE | RELIABLE | EASY</p>

  <svg class="shapes" width="726" height="1026" viewBox="0 0 726 1026" aria-hidden="true" style="pointer-events:none">
    <line x1="196" y1="914" x2="196" y2="1010" stroke="var(--line)" stroke-width="1"/>
    <line x1="24" y1="962" x2="180" y2="962" stroke="var(--line)" stroke-width="1"/>
    <line x1="212" y1="962" x2="372" y2="962" stroke="var(--line)" stroke-width="1"/>
  </svg>
  <div class="service" style="left:28px;top:918px">
    <svg width="28" height="28" viewBox="0 0 24 24" aria-hidden="true"><circle cx="12" cy="8" r="4" fill="none" stroke="var(--orange)" stroke-width="1.8"/><path d="M4 21c0-4.4 3.6-7 8-7s8 2.6 8 7" fill="none" stroke="var(--orange)" stroke-width="1.8"/></svg>
    <span>Consultation</span>
  </div>
  <div class="service" style="left:216px;top:918px">
    <svg width="28" height="28" viewBox="0 0 24 24" aria-hidden="true"><path d="M4 4l16 16M20 4L4 20" stroke="var(--orange)" stroke-width="2.4" stroke-linecap="round"/></svg>
    <span>Installation</span>
  </div>
  <div class="service" style="left:28px;top:972px">
    <svg width="28" height="28" viewBox="0 0 24 24" aria-hidden="true"><path d="M6 3h9l4 4v14H6z" fill="none" stroke="var(--orange)" stroke-width="1.8"/><path d="M12.5 9v9M14.5 10.5h-3a1.5 1.5 0 0 0 0 3h2a1.5 1.5 0 0 1 0 3h-3" fill="none" stroke="var(--orange)" stroke-width="1.5"/></svg>
    <span>Design</span>
  </div>
  <div class="service" style="left:216px;top:972px">
    <svg width="28" height="28" viewBox="0 0 24 24" aria-hidden="true"><path d="M4 14v-2a8 8 0 0 1 16 0v2" fill="none" stroke="var(--orange)" stroke-width="1.8"/><rect x="3" y="13" width="4" height="6" rx="1" fill="var(--orange)"/><rect x="17" y="13" width="4" height="6" rx="1" fill="var(--orange)"/><path d="M19 19c0 2-2 3-6 3" fill="none" stroke="var(--orange)" stroke-width="1.5"/></svg>
    <span>Support</span>
  </div>
</main>
</body>
</html>
```